Propose a revamped landing page

One template we like eg is https://www.tornavo.com but but cluttered Our logo and colors are attached to our logo and colors are printed on a white background what we have. So font usage ...
Number of Pages Required
1 page

```html
<!DOCTYPE html>
<html lang="en">
<head>
<meta charset="utf-8">
<title>Voltara – Always switch to the cheapest energy provider</title>
<link href="https://fonts.googleapis.com/css2?family=Montserrat:wght@600;700;800;900&family=Open+Sans:wght@400;600;700&display=swap" rel="stylesheet">
<style>
:root{
  --orange:#f7a11a;
  --orange-deep:#f07f12;
  --red:#ee4a2a;
  --ink:#2d333a;
  --text:#4d555e;
  --muted:#8a929b;
  --white:#ffffff;
  --paper:#f7f8fa;
  --footer:#3b424a;
  --link:#3aa7d8;
}
*{box-sizing:border-box;margin:0;padding:0}
html,body{width:1200px;height:3584px;overflow:hidden}
body{position:relative;background:var(--paper);font-family:'Open Sans',sans-serif;color:var(--text)}
.bands{position:absolute;left:0;top:0}
.abs{position:absolute}
h1,h2,h3,.brand,.step-no{font-family:'Montserrat',sans-serif}

/* nav */
.brand{font-weight:900;font-size:30px;color:var(--white);display:flex;align-items:center;gap:8px;letter-spacing:.5px}
.brand .dot{width:22px;height:22px;border-radius:50%;background:var(--white)}
.nav{left:80px;top:34px;width:1040px;display:flex;justify-content:space-between;align-items:center;z-index:2}
.nav ul{list-style:none;display:flex;gap:34px;align-items:center}
.nav a{color:var(--white);text-decoration:none;font-size:14px;font-weight:600}
.nav .menu-btn{width:34px;height:34px;border-radius:50%;background:var(--red);display:block}

/* hero */
.hero-title{left:80px;top:180px;width:620px;color:var(--white);font-size:46px;font-weight:800;line-height:1.15}
.hero-sub{left:80px;top:356px;width:520px;color:var(--white);font-size:17px;line-height:1.55}
.btn{display:inline-flex;align-items:center;gap:12px;background:var(--red);color:var(--white);font-weight:700;font-size:13px;text-transform:uppercase;letter-spacing:.5px;border-radius:26px;padding:12px 14px 12px 24px;text-decoration:none}
.btn .arrow{width:22px;height:22px;border-radius:50%;background:var(--white);display:flex;align-items:center;justify-content:center}
.hero-btn{left:80px;top:440px}
.figure-hero{left:790px;top:130px;width:260px;height:470px;border-radius:120px 120px 60px 60px;background:linear-gradient(160deg,#5fb4e6,#2e6fa3 60%,#2a4d70)}

/* how it works */
.section-title{font-size:38px;font-weight:800;color:var(--ink)}
.section-title.under{text-decoration:underline;text-decoration-thickness:4px;text-underline-offset:8px}
.how-title{left:120px;top:700px}
.step-card{background:var(--white);border-radius:10px;box-shadow:0 12px 34px rgba(40,50,70,.12);padding:96px 26px 30px}
.step-card h3{font-size:24px;font-weight:700;color:var(--ink);margin-bottom:12px}
.step-card p{font-size:14px;line-height:1.6;color:var(--muted)}
.step-card .icon{position:absolute;left:24px;top:-34px;width:104px;height:84px;border-radius:14px;background:linear-gradient(150deg,#cfe9f8,#88c6ea)}
.step-card .go{position:absolute;right:-18px;bottom:-22px;width:50px;height:50px;border-radius:50%;background:var(--red);display:flex;align-items:center;justify-content:center;box-shadow:0 8px 18px rgba(238,74,42,.35)}
.card-choose{left:150px;top:940px;width:290px;height:250px}
.card-upload{left:470px;top:830px;width:290px;height:250px}
.card-recline{left:780px;top:700px;width:270px;height:310px;padding-top:72px}

/* testimonials + pricing */
.quote{background:var(--white);border-radius:8px;box-shadow:0 12px 30px rgba(120,60,0,.2);padding:40px 28px 26px;font-size:14px;line-height:1.6;color:var(--text)}
.quote .mark{position:absolute;left:20px;top:-24px;width:46px;height:46px;border-radius:50%;background:linear-gradient(150deg,#cfe9f8,#88c6ea)}
.quote .name{margin-top:14px;font-weight:700;color:var(--link);font-size:14px}
.quote .role{color:var(--muted);font-size:12px}
.quote-1{left:170px;top:1450px;width:280px}
.quote-2{left:310px;top:1710px;width:290px}
.more{left:160px;top:1960px;color:var(--white);font-size:12px;font-weight:700;letter-spacing:1px;display:flex;align-items:center;gap:10px}
.more .arrow{width:20px;height:20px;border-radius:50%;background:var(--red)}
.powers-title{left:620px;top:1460px;width:460px;color:var(--white);font-size:36px;font-weight:800;line-height:1.2}
.powers-lead{left:620px;top:1565px;color:var(--white);font-size:19px;font-weight:700}
.price-list{left:620px;top:1620px;width:440px;list-style:none;color:var(--white)}
.price-list li{display:flex;gap:14px;font-size:14px;line-height:1.5;margin-bottom:22px}
.price-list .tick{flex:none;width:24px;height:24px;border-radius:50%;background:var(--white);display:flex;align-items:center;justify-content:center}
.price-list b{display:block}
.fineprint{left:620px;top:1910px;width:420px;color:var(--white);font-size:10px;line-height:1.5;opacity:.9}

/* become */
.become-title{left:120px;top:2250px;width:460px;line-height:1.2}
.steps{left:120px;top:2400px;width:470px}
.step{margin-bottom:30px}
.step-no{font-size:44px;font-weight:800;color:var(--ink);line-height:1}
.step h3{font-size:24px;font-weight:700;color:var(--ink);margin:2px 0 6px}
.step p{font-size:15px;color:var(--muted)}
.figure-become{left:610px;top:2160px;width:360px;height:640px;border-radius:160px 160px 80px 80px;background:linear-gradient(160deg,#5fb4e6,#2e6fa3 60%,#2a4d70)}

/* closing */
.closing{left:0;top:3060px;width:1200px;text-align:center;color:var(--white)}
.closing h2{font-size:40px;font-weight:800;line-height:1.25}
.closing p{font-size:15px;margin:22px auto 30px;width:620px;line-height:1.6}

/* footer */
.footer-brand{left:0;top:3420px;width:1200px;justify-content:center;color:var(--orange);font-size:56px}
.footer-brand .dot{width:34px;height:34px;background:var(--orange)}
.footer-links{left:0;top:3534px;width:1200px;display:flex;justify-content:center;gap:46px;list-style:none}
.footer-links a{color:var(--white);text-decoration:none;font-size:12px;font-weight:600}
</style>
</head>
<body>

<svg class="bands" width="1200" height="3584" viewBox="0 0 1200 3584" aria-hidden="true">
  <polygon points="0,0 1200,0 1200,520 0,660" fill="var(--orange)"/>
  <polygon points="0,1380 1200,1240 1200,2020 0,2120" fill="var(--orange)"/>
  <polygon points="0,2980 1200,2860 1200,3360 0,3360" fill="var(--orange)"/>
  <rect x="0" y="3360" width="1200" height="224" fill="var(--footer)"/>
</svg>

<div class="figure-hero abs" role="img" aria-label="Illustrated superhero mascot in a blue suit and cape flying"></div>

<header class="nav abs">
  <div class="brand">Voltara<span class="dot"></span></div>
  <ul>
    <li><a href="#">How it Works</a></li>
    <li><a href="#">Prices</a></li>
    <li><a href="#">FAQ</a></li>
    <li><a href="#">About Us</a></li>
    <li><a href="#">Questions</a></li>
    <li><a href="#">Experience</a></li>
    <li><a href="#">Shop</a></li>
    <li><span class="menu-btn"></span></li>
  </ul>
</header>

<h1 class="hero-title abs">Always Automatically Switch to the Cheapest Energy Provider</h1>
<p class="hero-sub abs">Gone are the days of bad deals, tedious rate comparison and boring exchange forms.</p>
<a class="btn hero-btn abs" href="#">Register now <span class="arrow"><svg width="10" height="10" viewBox="0 0 10 10"><path d="M2 5h6M5 2l3 3-3 3" stroke="#ee4a2a" stroke-width="1.8" fill="none"/></svg></span></a>

<h2 class="section-title under how-title abs">How It Works!</h2>

<article class="step-card card-choose abs">
  <span class="icon" role="img" aria-label="Illustration of a settings panel"></span>
  <h3>Choose</h3>
  <p>Set the automatic exchange service according to your wishes.</p>
  <span class="go"><svg width="18" height="14" viewBox="0 0 18 14"><path d="M1 7h14M10 2l5 5-5 5" stroke="#fff" stroke-width="2.2" fill="none"/></svg></span>
</article>
<article class="step-card card-upload abs">
  <span class="icon" role="img" aria-label="Illustration of a document upload"></span>
  <h3>Upload</h3>
  <p>Simply upload a financial statement, enter a few more personal details, and you're done.</p>
  <span class="go"><svg width="18" height="14" viewBox="0 0 18 14"><path d="M1 7h14M10 2l5 5-5 5" stroke="#fff" stroke-width="2.2" fill="none"/></svg></span>
</article>
<article class="step-card card-recline abs">
  <span class="icon" role="img" aria-label="Illustration of a reclining chair"></span>
  <h3>Recline</h3>
  <p>You do not have to do anything anymore. We make sure that from now on you always have the cheapest tariff on the market.</p>
  <span class="go"><svg width="18" height="14" viewBox="0 0 18 14"><path d="M1 7h14M10 2l5 5-5 5" stroke="#fff" stroke-width="2.2" fill="none"/></svg></span>
</article>

<blockquote class="quote quote-1 abs">
  <span class="mark"></span>
  Uncomplicated, smooth and very nice customer service. Great thing!
  <div class="name">Lena Hart</div>
  <div class="role">Member since 2019</div>
</blockquote>
<blockquote class="quote quote-2 abs">
  <span class="mark"></span>
  Great! I will pay over 400 euros less next year. I was skeptical, but everything worked perfectly.
  <div class="name">Clara Benn <span class="role">Member</span></div>
</blockquote>
<a class="more abs">MORE TESTIMONIALS <span class="arrow"></span></a>

<h2 class="powers-title abs">The Cheapest of All Super Powers</h2>
<p class="powers-lead abs">From 21 euros you are there</p>
<ul class="price-list abs">
  <li><span class="tick"><svg width="12" height="10" viewBox="0 0 12 10"><path d="M1 5l3.5 3.5L11 1" stroke="#f07f12" stroke-width="2" fill="none"/></svg></span><span>Service for electricity or gas (1 contract)<b>24 euros / year</b></span></li>
  <li><span class="tick"><svg width="12" height="10" viewBox="0 0 12 10"><path d="M1 5l3.5 3.5L11 1" stroke="#f07f12" stroke-width="2" fill="none"/></svg></span><span>Service for electricity and gas (2 contracts)<b>36 euros / year</b></span></li>
  <li><span class="tick"><svg width="12" height="10" viewBox="0 0 12 10"><path d="M1 5l3.5 3.5L11 1" stroke="#f07f12" stroke-width="2" fill="none"/></svg></span><span><b>The first fee will be charged only after your first change</b></span></li>
  <li><span class="tick"><svg width="12" height="10" viewBox="0 0 12 10"><path d="M1 5l3.5 3.5L11 1" stroke="#f07f12" stroke-width="2" fill="none"/></svg></span><span><b>Save up to 450 euros annually electricity and gas costs at the first change *</b></span></li>
</ul>
<p class="fineprint abs">* Average savings for an average household with 4,000 kWh of electricity and 20,000 kWh of gas per year compared to the local basic supplier tariff. Individual savings may vary.</p>

<h2 class="section-title under become-title abs">How do I become Voltara Hero?</h2>
<div class="steps abs">
  <div class="step"><div class="step-no">01</div><h3>Once login…</h3><p>…upload financial statement. Select preferences. Finish the registration.</p></div>
  <div class="step"><div class="step-no">02</div><h3>Automatic fare change</h3><p>We pick the cheapest fee for you and carry out the change automatically.</p></div>
  <div class="step"><div class="step-no">03</div><h3>Sit back and save money</h3><p>Always switch automatically to the low fee.</p></div>
</div>
<div class="figure-become abs" role="img" aria-label="Illustrated superhero mascot standing with hands on hips"></div>

<section class="closing abs">
  <h2>You sign up once and we'll do the rest.<br>All automatically.</h2>
  <p>We work only for you: in order to remain independent, we consciously do without commissions from energy providers.</p>
  <a class="btn" href="#">Register now <span class="arrow"><svg width="10" height="10" viewBox="0 0 10 10"><path d="M2 5h6M5 2l3 3-3 3" stroke="#ee4a2a" stroke-width="1.8" fill="none"/></svg></span></a>
</section>

<div class="brand footer-brand abs">Voltara<span class="dot"></span></div>
<ul class="footer-links abs">
  <li><a href="#">Conditions</a></li>
  <li><a href="#">Data Protection</a></li>
  <li><a href="#">Imprint</a></li>
</ul>

</body>
</html>
```